Zertifikat-Design und Garantieschein-Design für Uhrenmanufaktur gesucht
Zielgruppe
Wir sind eine Uhrenmanufaktur und fertigen hochwertige mechanische Armbanduhren in größten Teilen in Handarbeit.
Für die Auslieferung unserer Uhren brauchen wir ein Zertifikat und einen Garantieschein (jeweils 1 Blatt).
Unsere Zielgruppe sind gutverdienende Menschen zwischen 25 und 55 Jahren.
Aufgabenstellung
Es soll jeweils ein Zertifikat erstellt werden (1 Blatt - nur Vorderseite) und ein Garantieschein (1 Blatt - Vorder- und Rückseite). Alle Vorgaben, sowie Bilder der Uhren als Inspiration sind in der PDF enthalten.

```html
<!DOCTYPE html>
<html lang="de">
<head>
<meta charset="utf-8">
<title>HALDEN Uhrmacher – Zertifikat</title>
<link rel="stylesheet" href="https://fonts.googleapis.com/css2?family=Outfit:wght@300;400;600&display=swap">
<style>
  :root {
    --backdrop: #e4e5e5;
    --paper: #fbfcfc;
    --frame: #cfe5e6;
    --ink: #222628;
    --teal: #2a6470;
    --rule: #2f6875;
    --seal-light: #d9ebeb;
    --seal-mid: #9cc6c7;
    --seal-dark: #5f9799;
  }
  * { box-sizing: border-box; margin: 0; padding: 0; }
  html, body {
    width: 1200px; height: 1188px; overflow: hidden;
    background: var(--backdrop);
    font-family: "Outfit", sans-serif;
    color: var(--ink);
  }
  .certificate {
    position: absolute; left: 170px; top: 29px;
    width: 860px; height: 1130px;
    background: var(--frame);
    box-shadow: 0 14px 30px rgba(0,0,0,.12);
  }
  .certificate__sheet {
    position: absolute; inset: 32px;
    background: var(--paper);
  }
  .block { position: absolute; left: 47px; right: 47px; }
  .brand { top: 62px; text-align: center; }
  .brand__name {
    font-weight: 300; font-size: 66px; letter-spacing: 0; line-height: 1; color: var(--ink);
  }
  .brand__tagline {
    margin-top: 8px; font-weight: 300; font-size: 26px; letter-spacing: 2px; color: var(--ink);
  }
  .title {
    top: 222px; height: 66px;
    border-top: 1.5px solid var(--rule); border-bottom: 1.5px solid var(--rule);
    display: flex; align-items: center; justify-content: center; gap: 18px;
    font-size: 52px; line-height: 1; letter-spacing: 1.5px; white-space: nowrap;
  }
  .title__de { font-weight: 600; }
  .title__sep { font-weight: 300; color: var(--teal); }
  .title__en { font-weight: 300; }
  .specs { font-size: 15.5px; line-height: 23px; }
  .specs__row { display: flex; }
  .specs__label { width: 245px; }
  .specs--model { top: 356px; }
  .specs--parts { top: 555px; line-height: 22.6px; }
  b { font-weight: 600; }
  .slash { color: var(--teal); font-weight: 300; }
  .statement {
    top: 457px; padding: 8px 0 8px;
    border-top: 1.2px solid var(--rule); border-bottom: 1.2px solid var(--rule);
    font-size: 15.5px; line-height: 23px; color: var(--teal);
  }
  .parties { font-size: 15.5px; line-height: 23.5px; }
  .parties--buyer { top: 726px; }
  .parties--seller { top: 820px; }
  .party { display: grid; grid-template-columns: 99px 133px 224px 1fr; }
  .party__role { color: var(--teal); }
  .signing { top: 960px; font-size: 15.5px; }
  .signing__date {
    position: absolute; left: 2px; top: 0; width: 243px; height: 34px;
    border-bottom: 1px solid var(--rule); padding-left: 2px; padding-top: 8px;
  }
  .signing__sign {
    position: absolute; left: 291px; top: -30px; width: 242px; height: 64px;
    border-bottom: 1px solid var(--rule);
  }
  .signing__script {
    position: absolute; left: 0; top: 6px; width: 190px; height: 54px;
    background: radial-gradient(ellipse at 45% 60%, rgba(34,38,40,.16) 0%, rgba(34,38,40,.07) 45%, rgba(34,38,40,0) 72%);
  }
  .signing__caption { position: absolute; top: 46px; color: var(--teal); }
  .signing__caption--date { left: 2px; }
  .signing__caption--sign { left: 291px; }
  .seal {
    position: absolute; left: 627px; top: 929px;
    width: 124px; height: 124px; border-radius: 50%;
    background: linear-gradient(90deg, var(--seal-light) 0%, var(--seal-mid) 35%, var(--seal-dark) 50%, var(--seal-mid) 65%, var(--seal-light) 100%);
  }
</style>
</head>
<body>
  <main class="certificate">
    <div class="certificate__sheet">

      <header class="block brand">
        <div class="brand__name">HALDEN</div>
        <div class="brand__tagline">UHRMACHER</div>
      </header>

      <h1 class="block title">
        <span class="title__de">ZERTIFIKAT</span>
        <span class="title__sep">/</span>
        <span class="title__en">CERTIFICATE</span>
      </h1>

      <section class="block specs specs--model">
        <div class="specs__row"><span class="specs__label"><b>Modellname</b> <span class="slash">/</span> Model name:</span><span>Lorem ipsum dolor sit amet</span></div>
        <div class="specs__row"><span class="specs__label"><b>Referenznr.</b> <span class="slash">/</span> Reference No.:</span><span>12345/12345</span></div>
        <div class="specs__row"><span class="specs__label"><b>Kaliber</b> <span class="slash">/</span> Caliber:</span><span>Nullor dolores sit</span></div>
      </section>

      <p class="block statement">
        <b>Diese Uhr wurde hergestellt, montiert und einreguliert im HALDEN-Atelier in Dresden.</b> /<br>
        This watch was made, assembled and adjusted in the HALDEN atelier in Dresden, Germany.
      </p>

      <section class="block specs specs--parts">
        <div class="specs__row"><span class="specs__label"><b>Gehäuse</b> <span class="slash">/</span> Case:</span><span>Lorem ipsum dolor sit amet</span></div>
        <div class="specs__row"><span class="specs__label"><b>Glas</b> <span class="slash">/</span> Glass:</span><span>Nullor dolores sit</span></div>
        <div class="specs__row"><span class="specs__label"><b>Band</b> <span class="slash">/</span> Strap:</span><span>Sit lorem nullor, dolorem sit lorem</span></div>
        <div class="specs__row"><span class="specs__label"><b>Schließe</b> <span class="slash">/</span> Buckle:</span><span>Lorem ipsum dolor sit amet</span></div>
        <div class="specs__row"><span class="specs__label"><b>Zeiger</b> <span class="slash">/</span> Hands:</span><span>Nullor dolores sit</span></div>
        <div class="specs__row"><span class="specs__label"><b>Zifferblatt</b> <span class="slash">/</span> Dial:</span><span>Lorem ipsum dolor sit</span></div>
      </section>

      <section class="block parties parties--buyer">
        <div class="party">
          <span class="party__role"><b>Käufer</b> /</span><span><b>Name</b> <span class="slash">/</span> Name:</span><span>Loremus Ipsum</span><span></span>
          <span class="party__role">Purchaser</span><span><b>Straße</b> <span class="slash">/</span> Street:</span><span>Lorem ipsum dolor 12</span><span><b>PLZ</b> <span class="slash">/</span> Zip:&nbsp; 12345</span>
          <span></span><span><b>Stadt</b> <span class="slash">/</span> City:</span><span>Loremusipsum</span><span><b>Land</b> <span class="slash">/</span> Land: Doloremuso</span>
        </div>
      </section>

      <section class="block parties parties--seller">
        <div class="party">
          <span class="party__role"><b>Veräufer</b> /</span><span><b>Name</b> <span class="slash">/</span> Name:</span><span>Loremus Ipsum</span><span></span>
          <span class="party__role">Seller</span><span><b>Straße</b> <span class="slash">/</span> Street:</span><span>Lorem ipsum dolor 12</span><span><b>PLZ</b> <span class="slash">/</span> Zip:&nbsp; 12345</span>
          <span></span><span><b>Stadt</b> <span class="slash">/</span> City:</span><span>Loremusipsum</span><span><b>Land</b> <span class="slash">/</span> Land: Doloremuso</span>
        </div>
      </section>

      <footer class="block signing">
        <div class="signing__date">01. August 2022</div>
        <div class="signing__sign">
          <div class="signing__script" role="img" aria-label="Handschriftliche Unterschrift"></div>
        </div>
        <div class="signing__caption signing__caption--date"><b>Ausstellungsdatum</b> / Date of issue</div>
        <div class="signing__caption signing__caption--sign"><b>Unterschrift</b> / Sign</div>
      </footer>

      <div class="seal" role="img" aria-label="Prägesiegel"></div>

    </div>
  </main>
</body>
</html>
```